Guava Energy Bar Logo and Packaging Art for New Brand/Product

I want to design product packaging for a Guava energy bar that is made primarily from the guava fruit grown on Hawaii. It is a high energy bar designed for quick energy for athletes, hikers, cyclists and adventurers. I want to play in the K.I.E.E and call the bar the "Kiwi (kingliest) In Every Era." It will be made from real Guava and wrapped in a compostable leaf wrapper, gluten free and vegan friendly. I want to play on the fact that Guava is a superfood packed with essential vitamins and minerals and free from artificial colours and preservatives.
Target Market(s)
Athletes, Hikers, Cyclists, Runners, Climbers, Triathletes and Adventurers
Requirements
Must have
- I want to make the K.I.E.E. (kingliest in every era) woven in the brand and logo with a strong reference to Guava; the super fruit!
Nice to have
- Take a look at the brand and packaging for Trekko Bars

```html
<!DOCTYPE html>
<html lang="en">
<head>
<meta charset="utf-8">
<title>Guava Energy Bar – KIEE Pack Front</title>
<link rel="stylesheet" href="https://fonts.googleapis.com/css2?family=Russo+One&family=Audiowide&family=Mulish:ital,wght@0,300;1,800&display=swap">
<style>
  :root {
    --page: #ffffff;
    --pack-deep: #064206;
    --pack-mid: #0f6a12;
    --pack-glow: #3fbf2a;
    --neon: #4cff14;
    --guava-pink: #ff7f88;
    --guava-rind: #c4e07a;
    --band-line: #f07a7a;
  }
  * { box-sizing: border-box; margin: 0; padding: 0; }
  html, body {
    width: 1200px; height: 1200px; overflow: hidden;
    background: var(--page);
  }
  .canvas { position: relative; width: 1200px; height: 1200px; }

  .pack-front {
    position: absolute; left: 327px; top: 217px;
    width: 553px; height: 773px; overflow: hidden;
    background:
      radial-gradient(ellipse 60% 45% at 50% 62%, rgba(63,191,42,.75), rgba(63,191,42,0) 70%),
      linear-gradient(180deg, var(--pack-mid) 0%, var(--pack-deep) 100%);
  }

  .energy-ring {
    position: absolute; left: 195px; top: 30px; width: 162px; height: 162px;
    border-radius: 50%;
    background: radial-gradient(circle, rgba(76,255,20,0) 45%, rgba(76,255,20,.85) 58%, rgba(76,255,20,0) 72%);
  }

  .product-band {
    position: absolute; left: 18px; top: 84px; width: 517px; height: 64px;
    background: linear-gradient(90deg, rgba(76,255,20,0), rgba(76,255,20,.35) 50%, rgba(76,255,20,0));
    border-top: 1px solid var(--band-line);
    border-bottom: 1px solid var(--band-line);
    display: flex; align-items: center; justify-content: center;
  }
  .product-name {
    font-family: "Russo One", sans-serif; font-size: 42px; letter-spacing: 1px;
    color: var(--pack-deep); -webkit-text-stroke: 1.5px var(--neon);
    transform: skewX(-12deg);
  }

  .brand-name {
    position: absolute; left: 0; top: 212px; width: 553px;
    text-align: center;
    font-family: "Russo One", sans-serif; font-size: 195px; line-height: 1;
    letter-spacing: 4px; color: var(--guava-pink);
  }

  .guava-art {
    position: absolute; left: 158px; top: 288px; width: 180px; height: 155px;
    border-radius: 50%;
    background: linear-gradient(120deg, var(--guava-rind) 0%, var(--guava-rind) 45%, var(--guava-pink) 100%);
  }

  .brand-tagline {
    position: absolute; left: 0; top: 436px; width: 553px;
    text-align: center;
    font-family: "Russo One", sans-serif; font-size: 57px; line-height: 1.2;
    color: var(--guava-pink);
  }

  .activity-row {
    position: absolute; left: 38px; top: 522px; width: 475px; height: 46px;
  }
  .activity-row svg { display: block; }

  .audience {
    position: absolute; left: 0; top: 572px; width: 553px;
    text-align: center; color: var(--neon);
    font-family: "Audiowide", sans-serif;
  }
  .audience .lead { font-size: 22px; line-height: 30px; }
  .audience .list { font-size: 34px; line-height: 38px; letter-spacing: -.5px; }
  .audience .small { font-size: 19px; }

  .rule {
    position: absolute; left: 38px; top: 688px; width: 475px; height: 1px;
    background: linear-gradient(90deg, rgba(76,255,20,0), var(--neon) 20%, var(--neon) 80%, rgba(76,255,20,0));
  }

  .net-weight {
    position: absolute; left: 0; top: 712px; width: 553px;
    text-align: center; color: var(--guava-pink);
    font-family: "Mulish", sans-serif; font-size: 25px; font-weight: 300;
  }
  .net-weight strong { font-weight: 800; font-style: italic; }
</style>
</head>
<body>
<div class="canvas">
  <section class="pack-front">
    <div class="energy-ring" role="img" aria-label="Glowing green electric energy ring"></div>

    <div class="product-band">
      <span class="product-name">GUAVA ENERGY BAR</span>
    </div>

    <h1 class="brand-name">KIEE</h1>

    <div class="guava-art" role="img" aria-label="Whole green guava with a cut pink half and leaves"></div>

    <p class="brand-tagline">kiwi in every era</p>

    <div class="activity-row">
      <svg width="475" height="46" viewBox="0 0 475 46" role="img" aria-label="Activity badges: running, hiking, cycling, climbing, swimming">
        <line x1="0" y1="23" x2="475" y2="23" stroke="var(--neon)" stroke-width="1"/>
        <g fill="var(--guava-pink)" stroke="var(--neon)" stroke-width="2">
          <circle cx="119" cy="23" r="22"/>
          <circle cx="178" cy="23" r="22"/>
          <circle cx="238" cy="23" r="22"/>
          <circle cx="297" cy="23" r="22"/>
          <circle cx="357" cy="23" r="22"/>
        </g>
      </svg>
    </div>

    <div class="audience">
      <p class="lead">for quick energy for</p>
      <p class="list">athletes, hikers, cyclists</p>
      <p class="list"><span class="small">and</span> adventurers</p>
    </div>

    <div class="rule"></div>

    <p class="net-weight">Net Wt. <strong>1.59 oz.</strong> (45g)</p>
  </section>
</div>
</body>
</html>
```